a4 size poster for theatre school

I am looking for an eye catching poster for my theatre school - Bright Lantern Stage school - View our website here for the style we have already www.brightlanternstage.co.uk

Wording needs to include;

* Award Winning, Accredited, Affordable Performing Arts Classes taught by Leading Industry Experts

* Ages 4- 21 years

* All classes contain all three disciplines of Drama, Singing & Dance keeping cost low and enjoyment high

* Classes offered;
Drama
QWERN
Singing
PBSO dance
Freestyle Ballet
Freestyle Tap
Contemporary
Street
Jazz Musical Theatre

* FREE casting agency for TV and Theatre Available. Ten pupils currently performing in West End Productions, 8 pupils currently on screen in TV commercials, several pupils currently working on film & TV projects for Zentrovia, Velmora Plus & Kestrel TV.

* Optional PBSO and QWERN exams

* Unparalleled performance opportunities both locally and in the West End

Our quality training is evident in our pupils success

* Now in our successful 17th Year!

* Awarded recognition from the Board for Youth Stagecraft and Movement Studies - The industry regulator for children's performing arts training.

Target Market(s)

Parents & Children ages 4-21 years

Industry/Entity Type

Performing arts

Font styles to use
Other font styles liked:
• Arvo

Colors
EB3D1F
EC4F4E
F09395
F8D3D4
FCEDEE
6B429C
8869AF
B7A5CE
E3DAEB
F3F0F8

Requirements
Must have
• A good mix of photo's pf boys & girls. Different ethnicities. Different ages
Nice to have
• Wording very clear
Should not have
• Too many words

```html
<!DOCTYPE html>
<html lang="en">
<head>
<meta charset="utf-8">
<title>Bright Lantern Stage school – Poster</title>
<link href="https://fonts.googleapis.com/css2?family=Arvo:wght@400;700&display=swap" rel="stylesheet">
<style>
  :root {
    --backdrop: #cbcbcb;
    --navy: #1b1846;
    --stage-deep: #141a5c;
    --stage-glow: #3a4fb8;
    --yellow: #e9e25c;
    --red: #e63c22;
    --red-soft: #f4a08e;
    --white: #ffffff;
    --ink: #1b1846;
    --class-text: #e9e6f2;
    --box-line: #5b5878;
    --badge-teal: #25a0c0;
  }
  * { margin: 0; padding: 0; box-sizing: border-box; }
  html, body { width: 961px; height: 1200px; overflow: hidden; }
  body { background: var(--backdrop); position: relative; font-family: 'Arvo', serif; }

  .poster {
    position: absolute; left: 157px; top: 142px;
    width: 1000px; height: 1415px;
    transform: scale(0.6476); transform-origin: top left;
    background: var(--white); overflow: hidden;
  }
  .abs { position: absolute; }

  .hero-photo {
    left: 0; top: 0; width: 1000px; height: 642px;
    background:
      radial-gradient(ellipse at 55% 45%, #8a3a8c 0%, rgba(138,58,140,0) 35%),
      radial-gradient(ellipse at 20% 25%, var(--stage-glow) 0%, rgba(58,79,184,0) 45%),
      linear-gradient(180deg, #1a1f6a 0%, var(--stage-deep) 60%, #2a3a90 100%);
  }
  .tagline {
    left: 0; width: 1000px; top: 42px; text-align: center;
    color: var(--white); font-weight: 700; font-size: 26px; letter-spacing: 8px;
  }
  .brand {
    left: 700px; top: 120px; width: 270px;
    display: flex; align-items: center; gap: 12px;
    color: var(--red); font-weight: 700; font-size: 34px; line-height: 1.05;
  }
  .brand-mark { width: 30px; height: 30px; border-radius: 50%; background: var(--yellow); flex: none; }

  .promises { left: 72px; top: 352px; list-style: none; }
  .promises li {
    display: flex; align-items: center; gap: 12px;
    color: var(--white); font-weight: 700; font-size: 58px; line-height: 59px;
    text-shadow: 3px 3px 4px rgba(0,0,0,0.45);
  }
  .promises svg { width: 42px; height: 42px; flex: none; }

  .expert-band {
    left: 0; top: 544px; width: 720px; height: 98px;
    background: var(--yellow); color: var(--ink); padding: 8px 0 0 70px;
  }
  .expert-band .lead { font-size: 35px; line-height: 36px; }
  .expert-band .strong { font-size: 33px; line-height: 34px; font-weight: 700; }

  .age-badge {
    left: 692px; top: 494px; width: 176px; height: 176px; border-radius: 50%;
    background: var(--red); color: var(--white); z-index: 3;
    display: flex; flex-direction: column; align-items: center; justify-content: center;
    font-weight: 700; font-size: 38px; line-height: 35px; text-align: center;
  }

  .classes-panel { left: 0; top: 642px; width: 1000px; height: 288px; background: var(--navy); }
  .classes-frame {
    left: 45px; top: 51px; width: 904px; height: 195px;
    border: 4px solid var(--red);
  }
  .classes-title {
    left: 0; width: 1000px; top: 35px; text-align: center;
  }
  .classes-title span {
    background: var(--navy); padding: 0 22px;
    color: var(--white); font-weight: 700; font-size: 32px;
  }
  .class-list {
    left: 77px; top: 87px; width: 880px;
    display: grid; grid-template-columns: 181px 305px 1fr; row-gap: 9px;
    list-style: none;
  }
  .class-list li {
    display: flex; align-items: center; gap: 13px;
    color: var(--class-text); font-size: 32px; line-height: 37px; white-space: nowrap;
  }
  .class-list svg { width: 27px; height: 27px; flex: none; }

  .photo { background: linear-gradient(135deg, var(--c1), var(--c2)); }
  .photo-kids-yellow { --c1: #e9c95a; --c2: #d59a6c; }
  .photo-costumes { --c1: #b9a8d8; --c2: #6b4a3a; }
  .photo-stage-red { --c1: #3a2a2a; --c2: #b8503a; }
  .photo-dance-group { --c1: #1d2050; --c2: #5a5a90; }
  .photo-car-scene { --c1: #3a2a30; --c2: #c0443a; }

  .casting {
    left: 370px; top: 1124px; width: 630px; height: 177px;
    background: var(--red); color: var(--white); padding: 26px 14px 0 28px;
    font-size: 17.5px; line-height: 27px; letter-spacing: -0.4px;
  }
  .casting .headline { font-weight: 700; }
  .casting .arrow { color: var(--red-soft); }

  .accreditation-badge { left: 34px; top: 1313px; width: 304px; height: 62px; background: var(--badge-teal); }
  .accreditation-note {
    left: 350px; top: 1312px; width: 322px;
    color: #111; font-size: 15.5px; line-height: 20px; letter-spacing: -0.2px;
  }
  .exams-box {
    left: 675px; top: 1302px; width: 291px; height: 113px; background: var(--yellow);
    color: var(--ink); font-size: 28px; line-height: 30px; text-align: center;
    display: flex; align-items: center; justify-content: center; padding-bottom: 8px;
  }
  .exams-box b { font-weight: 700; }
</style>
</head>
<body>
<div class="poster">
  <div class="abs hero-photo" role="img" aria-label="Stage photo of young dancers leaping under blue spotlights"></div>
  <p class="abs tagline">NOW IN OUR SUCCESSFUL 17TH YEAR!</p>
  <div class="abs brand"><span class="brand-mark"></span><span>Bright Lantern Stage</span></div>

  <ul class="abs promises">
    <li><svg viewBox="0 0 42 42"><rect width="42" height="42" rx="4" fill="#fff"/><path d="M9 22l8 8 16-17" fill="none" stroke="#1b1846" stroke-width="6"/></svg>Award Winning</li>
    <li><svg viewBox="0 0 42 42"><rect width="42" height="42" rx="4" fill="#fff"/><path d="M9 22l8 8 16-17" fill="none" stroke="#1b1846" stroke-width="6"/></svg>Accredited</li>
    <li><svg viewBox="0 0 42 42"><rect width="42" height="42" rx="4" fill="#fff"/><path d="M9 22l8 8 16-17" fill="none" stroke="#1b1846" stroke-width="6"/></svg>Affordable</li>
  </ul>

  <div class="abs expert-band">
    <p class="lead">Performing Arts Classes Taught By</p>
    <p class="strong">Leading Industry Experts</p>
  </div>

  <section class="abs classes-panel">
    <div class="abs classes-frame"></div>
    <h2 class="abs classes-title"><span>CLASSES OFFERED</span></h2>
    <ul class="abs class-list">
      <li><svg viewBox="0 0 27 27"><rect x="1" y="1" width="25" height="25" rx="3" fill="none" stroke="#5b5878" stroke-width="2"/><path d="M7 14l5 5 9-10" fill="none" stroke="#5b5878" stroke-width="2.5"/></svg>Drama</li>
      <li><svg viewBox="0 0 27 27"><rect x="1" y="1" width="25" height="25" rx="3" fill="none" stroke="#5b5878" stroke-width="2"/><path d="M7 14l5 5 9-10" fill="none" stroke="#5b5878" stroke-width="2.5"/></svg>PBSO dance</li>
      <li><svg viewBox="0 0 27 27"><rect x="1" y="1" width="25" height="25" rx="3" fill="none" stroke="#5b5878" stroke-width="2"/><path d="M7 14l5 5 9-10" fill="none" stroke="#5b5878" stroke-width="2.5"/></svg>Contemporary</li>
      <li><svg viewBox="0 0 27 27"><rect x="1" y="1" width="25" height="25" rx="3" fill="none" stroke="#5b5878" stroke-width="2"/><path d="M7 14l5 5 9-10" fill="none" stroke="#5b5878" stroke-width="2.5"/></svg>QWERN</li>
      <li><svg viewBox="0 0 27 27"><rect x="1" y="1" width="25" height="25" rx="3" fill="none" stroke="#5b5878" stroke-width="2"/><path d="M7 14l5 5 9-10" fill="none" stroke="#5b5878" stroke-width="2.5"/></svg>Freestyle Ballet</li>
      <li><svg viewBox="0 0 27 27"><rect x="1" y="1" width="25" height="25" rx="3" fill="none" stroke="#5b5878" stroke-width="2"/><path d="M7 14l5 5 9-10" fill="none" stroke="#5b5878" stroke-width="2.5"/></svg>Street</li>
      <li><svg viewBox="0 0 27 27"><rect x="1" y="1" width="25" height="25" rx="3" fill="none" stroke="#5b5878" stroke-width="2"/><path d="M7 14l5 5 9-10" fill="none" stroke="#5b5878" stroke-width="2.5"/></svg>Singing</li>
      <li><svg viewBox="0 0 27 27"><rect x="1" y="1" width="25" height="25" rx="3" fill="none" stroke="#5b5878" stroke-width="2"/><path d="M7 14l5 5 9-10" fill="none" stroke="#5b5878" stroke-width="2.5"/></svg>Freestyle Tap</li>
      <li><svg viewBox="0 0 27 27"><rect x="1" y="1" width="25" height="25" rx="3" fill="none" stroke="#5b5878" stroke-width="2"/><path d="M7 14l5 5 9-10" fill="none" stroke="#5b5878" stroke-width="2.5"/></svg>Jazz Musical Theatre</li>
    </ul>
  </section>

  <div class="abs age-badge"><span>Ages</span><span>4-21</span><span>years</span></div>

  <div class="abs photo photo-kids-yellow" style="left:13px;top:941px;width:240px;height:177px" role="img" aria-label="Young children in costumes on a yellow stage"></div>
  <div class="abs photo photo-costumes" style="left:258px;top:941px;width:240px;height:177px" role="img" aria-label="Children in period costumes performing"></div>
  <div class="abs photo photo-stage-red" style="left:503px;top:941px;width:239px;height:177px" role="img" aria-label="Young performer singing in front of a chorus"></div>
  <div class="abs photo photo-dance-group" style="left:747px;top:941px;width:241px;height:177px" role="img" aria-label="Teen dance group performing on stage"></div>
  <div class="abs photo photo-car-scene" style="left:13px;top:1124px;width:353px;height:177px" role="img" aria-label="Musical theatre scene with a red car on stage"></div>

  <div class="abs casting">
    <p class="headline">FREE casting agency for TV and Theatre Available.</p>
    <p><span class="arrow">»</span> 10 pupils currently performing in West End Productions</p>
    <p><span class="arrow">»</span> 8 pupils currently on screen in TV commercials</p>
    <p><span class="arrow">»</span> Several working on film &amp; TV projects for Zentrovia, Velmora Plus &amp; Kestrel TV.</p>
  </div>

  <div class="abs accreditation-badge"></div>
  <p class="abs accreditation-note">Awarded recognition from the Board for Youth Stagecraft and Movement Studies - The industry regulator for children's performing arts training.</p>
  <div class="abs exams-box"><p>Optional <b>PBSO &amp;<br>QWERN</b> exams</p></div>
</div>
</body>
</html>
```